Gordon Pellbrook Consulting - Web Design Project

We need a web design for my new edgy consulting business specializing in innovation, technology and strategy.

It is our personal goal to turn each client into raving fans by helping them achieve their own business goals and aspirations through assisting them in raising their own innovation and marketing standards.

We provide our personalised and state-of-the-art services to our clients and boards who represent some of the world greatest innovative thinkers.
Updates

Here is some other information which may help shape your thinking.

I've had direct Involvement in the development of the following iPad, iPhone Applications and websites

FarbeyondOzlands.com (TerraLink platform) by Voyage Bureau
http://farbeyondozlands.example.au

Sail Verve by Bright Voyaging
https://apps.example-store.com/au/app/sail-verve/id100000001

uRedlandTR by Travel Territory Board
https://apps.example-store.com/au/app/uredlandtr/id100000002

Wexmoor Trips
http://www.wexmoortrips.example.au

Trek Mapper by Voyage Bureau
http://apps.example-store.com/au/app/trek-mapper/id100000003

Sunward by Sunward Travel Office
https://apps.example-store.com/au/app/sunward/id100000004

Upper Fernridge Valley Route by Visit Coastlands
https://apps.example-store.com/au/app/upper-fernridge-valley-route/id100000005

Wanderer Path by Travel Territory Board and Southern Plains Travel Council
https://apps.example-store.com/au/app/wanderers-path-grand-journey/id100000006

Gordon Pellbrook Consulting (GPC)
November 2012 – Present (8 months)Brisbane, Sydney, Canberra

Gordon’s consults to Small-to-Medium Enterprises (SME) and Government organisations on business strategy, technology strategy, risk mitigation, disruptive technology and innovation in the workplace.

Gordon’s consultancy mantra is that we cannot divorce economic life from cultural life particularly in an era when social capital may be as important as physical capital in business.

Reason: request from designers, I want to see their best efforts

Target Market(s)

35+

Industry/Entity Type

Business

Requirements
Must have
• Please use some of the personal image(s) contained in the zip files which can be downloaded from here

http://filedrop.example/k9Xq2Lm
http://filedrop.example/p4Rt7Vn
http://filedrop.example/z8Hw3Bc
Nice to have
• Black, Sleek design, maybe minimalist. Nice to have a Pixelle for the design. Nice to have it easily ported to Wordpress or be a modified Wordpress template. HTML 5, responsive design

```html
<!DOCTYPE html>
<html lang="en">
<head>
<meta charset="utf-8">
<title>Gordon Pellbrook Consulting</title>
<link rel="stylesheet" href="https://fonts.googleapis.com/css2?family=Roboto+Condensed:wght@300;400;700&display=swap">
<style>
  :root {
    --sky-light: #d2c2c6;
    --sky-mid: #8d7f98;
    --city-mid: #5e5b82;
    --city-dark: #2b2c48;
    --text-white: #ffffff;
    --accent-blue: #2f8fd8;
    --curl-cyan: #14a9cf;
    --curl-white: #f4f7f8;
    --curl-shade: #b9c4c9;
    --hint-text: #0a5f78;
    --skin-tone: #c9a08c;
    --suit-tone: #8fa3bb;
    --shirt-tone: #a9c3dc;
  }
  * { margin: 0; padding: 0; box-sizing: border-box; }
  html, body { width: 1200px; height: 800px; overflow: hidden; background: var(--city-dark); }
  .landing {
    position: relative;
    width: 1200px;
    height: 800px;
    overflow: hidden;
    font-family: "Roboto Condensed", "Arial Narrow", sans-serif;
  }
  .city-backdrop {
    position: absolute;
    inset: 0;
    background:
      radial-gradient(ellipse at 50% 0%, rgba(230,215,215,0.55) 0%, rgba(230,215,215,0) 45%),
      linear-gradient(180deg, var(--sky-light) 0%, var(--sky-mid) 14%, var(--city-mid) 38%, #4a4a70 65%, var(--city-dark) 100%);
  }
  .city-backdrop::after {
    content: "";
    position: absolute;
    inset: 0;
    background: radial-gradient(ellipse at 50% 45%, rgba(0,0,0,0) 40%, rgba(20,20,40,0.45) 100%);
  }
  .brand {
    position: absolute;
    z-index: 2;
    top: 200px;
    left: 0;
    width: 100%;
    text-align: center;
    font-weight: 700;
    font-size: 64px;
    letter-spacing: -1px;
    color: var(--text-white);
    text-shadow: 0 2px 6px rgba(0,0,0,0.35);
  }
  .brand .brand-accent { color: var(--accent-blue); }
  .mantra {
    position: absolute;
    z-index: 2;
    top: 313px;
    left: 0;
    width: 100%;
    text-align: center;
    font-weight: 300;
    font-size: 36px;
    line-height: 53px;
    color: var(--text-white);
    text-shadow: 0 1px 4px rgba(0,0,0,0.35);
  }
  .portrait {
    position: absolute;
    z-index: 1;
    left: 57px;
    top: 436px;
    width: 461px;
    height: 364px;
  }
  .enter-curl {
    position: absolute;
    right: 0;
    bottom: 0;
    width: 260px;
    height: 150px;
  }
  .enter-hint {
    position: absolute;
    z-index: 2;
    right: 16px;
    bottom: 12px;
    text-align right;
    text-align: right;
    font-weight: 400;
    font-size: 16px;
    line-height: 28px;
    color: var(--hint-text);
  }
</style>
</head>
<body>
  <main class="landing">
    <div class="city-backdrop" role="img" aria-label="Blurred aerial view of a city skyline in muted purple tones"></div>

    <h1 class="brand">Gordon Pellbrook <span class="brand-accent">Consulting</span></h1>

    <p class="mantra">
      We cannot divorce economic life from cultural life<br>
      particularly in an era when social capital may be as important<br>
      as physical capital in business.
    </p>

    <svg class="portrait" viewBox="0 0 461 364" role="img" aria-label="Portrait of Gordon Pellbrook in a light grey suit and tie">
      <path d="M0,364 L0,300 C20,250 90,225 150,205 L290,205 C360,225 440,250 461,300 L461,364 Z" fill="var(--suit-tone)"/>
      <path d="M165,205 L275,205 L245,364 L195,364 Z" fill="var(--shirt-tone)"/>
      <ellipse cx="203" cy="115" rx="88" ry="115" fill="var(--skin-tone)"/>
    </svg>

    <svg class="enter-curl" viewBox="0 0 260 150" aria-hidden="true">
      <defs>
        <linearGradient id="curlFold" x1="0" y1="1" x2="1" y2="0">
          <stop offset="0" stop-color="var(--curl-shade)"/>
          <stop offset="0.45" stop-color="var(--curl-white)"/>
          <stop offset="1" stop-color="var(--curl-shade)"/>
        </linearGradient>
      </defs>
      <polygon points="10,150 260,20 260,150" fill="var(--curl-cyan)"/>
      <path d="M10,150 C90,110 170,60 260,20 C225,60 215,80 215,105 C170,115 95,135 10,150 Z" fill="url(#curlFold)"/>
    </svg>
    <p class="enter-hint">swipe<br>or click to enter</p>
  </main>
</body>
</html>
```